Courier Business - Wordpress Design Project

Looking for a designer that can develop a 5 page clean website for a company I have a steak in,

http://parcel-brisk.com.au/

is the current website and I looks terrible,

The logo is hosted on the current site

Target Market(s)

Business to Business

Industry/Entity Type

Business

Requirements
Must have
• Clean, aesthetic and use free stock images

A google map with the office location

```html
<!DOCTYPE html>
<html lang="en">
<head>
<meta charset="utf-8">
<title>Parcel Brisk Couriers</title>
<link href="https://fonts.googleapis.com/css2?family=Arimo:wght@400;700&display=swap" rel="stylesheet">
<style>
  :root {
    --navy: #1b4a6e;
    --navy-dark: #123a58;
    --navy-light: #2b6690;
    --orange: #f05a28;
    --ink: #444444;
    --text: #4d4d4d;
    --panel-top: #5a5a5a;
    --panel-bottom: #7b7b7b;
    --white: #ffffff;
    --icon: #3a3a3a;
  }
  * { box-sizing: border-box; margin: 0; padding: 0; }
  html, body { width: 960px; height: 1200px; overflow: hidden; background: var(--white); }
  body { font-family: "Arimo", Arial, sans-serif; color: var(--text); position: relative; }

  .site-header { position: absolute; top: 0; left: 0; width: 960px; height: 150px; }
  .brand { position: absolute; left: 62px; top: 40px; display: flex; align-items: center; gap: 12px; }
  .brand-mark { width: 44px; height: 44px; border-radius: 50%; background: var(--navy); }
  .brand-name { font-size: 28px; font-weight: 700; color: var(--ink); letter-spacing: 0.5px; line-height: 1.1; }
  .social { position: absolute; right: 56px; top: 18px; display: flex; gap: 7px; list-style: none; }
  .social li { width: 25px; height: 25px; border-radius: 50%; background: var(--icon); }
  .call { position: absolute; right: 56px; top: 70px; display: flex; align-items: center; gap: 8px; font-size: 19px; font-weight: 700; }
  .call-label { color: var(--orange); }
  .call-number { color: #111; }

  .main-nav { position: absolute; left: 55px; top: 159px; width: 850px; height: 52px; border-radius: 6px;
    background: linear-gradient(to bottom, var(--navy-light), var(--navy) 45%, var(--navy-dark)); }
  .main-nav ul { list-style: none; display: flex; justify-content: center; align-items: center; height: 100%; }
  .main-nav li { color: var(--white); font-size: 16.5px; padding: 0 17px; position: relative; }
  .main-nav li + li::before { content: "|"; position: absolute; left: -3px; color: var(--orange); }

  .hero-photo { position: absolute; left: 55px; top: 228px; width: 589px; height: 295px; border-radius: 8px;
    background: linear-gradient(to bottom, #c9cbcc 0%, #e2e3e3 45%, #9a9b9b 70%, #6d6e6e 100%); }
  .tracking { position: absolute; left: 661px; top: 228px; width: 244px; height: 295px; border-radius: 6px;
    background: linear-gradient(to bottom, var(--panel-top), var(--panel-bottom)); padding: 12px 13px; }
  .tracking h2 { color: var(--orange); font-size: 19px; font-weight: 700; margin-bottom: 14px; }
  .tracking p { color: var(--white); font-size: 15.5px; line-height: 20px; margin-bottom: 22px; }
  .field { display: block; width: 217px; height: 31px; border-radius: 7px; background: var(--white);
    color: #aaaaaa; font-size: 15px; padding: 7px 12px; margin-bottom: 30px; }

  .slogan { position: absolute; left: 57px; top: 540px; width: 846px; height: 47px; }
  .slogan svg { position: absolute; inset: 0; }
  .slogan span { position: absolute; top: 7px; font-size: 29px; font-weight: 700; }
  .slogan .slogan-name { left: 36px; color: var(--orange); }
  .slogan .slogan-line { right: 50px; color: var(--navy-dark); }

  .welcome { position: absolute; left: 61px; top: 613px; width: 840px; }
  .welcome h1 { font-size: 19px; font-weight: 700; color: var(--ink); margin-bottom: 18px; }
  .welcome p { font-size: 15.5px; line-height: 20px; color: var(--text); }

  .features { position: absolute; left: 0; top: 833px; width: 960px; }
  .feature { position: absolute; width: 200px; text-align: center; }
  .feature-dot { width: 66px; height: 66px; border-radius: 50%; background: var(--navy); margin: 0 auto 18px; }
  .feature h3 { font-size: 26px; font-weight: 700; color: var(--ink); margin-bottom: 6px; }
  .feature li { list-style: none; font-size: 16px; line-height: 20px; color: var(--text); }

  .newsletter { position: absolute; left: 60px; top: 1077px; width: 845px; display: flex; align-items: center; }
  .newsletter-text { font-size: 19px; color: var(--ink); }
  .newsletter-field { margin-left: 12px; width: 209px; height: 30px; border: 1.5px solid var(--orange); border-radius: 6px;
    color: #bbbbbb; font-size: 15px; padding: 5px 9px; }
  .newsletter-submit { margin-left: 8px; width: 89px; height: 31px; background: var(--navy); color: var(--white);
    border-radius: 4px; font-size: 19px; text-align: center; line-height: 31px; }

  .site-footer { position: absolute; left: 0; top: 1136px; width: 960px; height: 64px;
    background: linear-gradient(to bottom, var(--navy-dark), var(--navy) 60%, var(--navy-light)); color: var(--white); }
  .footer-links { list-style: none; display: flex; position: absolute; left: 64px; top: 10px; font-size: 16px; }
  .footer-links li + li::before { content: "|"; margin: 0 9px; }
  .copyright { position: absolute; left: 62px; top: 44px; font-size: 12.5px; }
</style>
</head>
<body>
  <header class="site-header">
    <div class="brand">
      <span class="brand-mark"></span>
      <span class="brand-name">Parcel Brisk Couriers</span>
    </div>
    <ul class="social" aria-label="Social links">
      <li></li><li></li><li></li><li></li><li></li><li></li>
    </ul>
    <div class="call">
      <svg width="24" height="18" viewBox="0 0 24 18" aria-hidden="true">
        <path d="M2 6 Q12 -2 22 6 L19 8 L16 5 L8 5 L5 8 Z" fill="var(--navy)"/>
        <rect x="4" y="9" width="16" height="8" rx="2" fill="var(--navy)"/>
        <circle cx="12" cy="13" r="2.3" fill="#fff"/>
      </svg>
      <span class="call-label">Call NOW:</span>
      <span class="call-number">01632 960 418</span>
    </div>
  </header>

  <nav class="main-nav">
    <ul>
      <li>Home</li><li>About Us</li><li>Services</li><li>Locations</li><li>Technology</li><li>Careers</li><li>Contact</li>
    </ul>
  </nav>

  <div class="hero-photo" role="img" aria-label="Photo of a white branded delivery truck parked under a cloudy sky"></div>

  <aside class="tracking">
    <h2>Parcel Tracking</h2>
    <p>You can track your parcel by entering your tracking number and the delivery postcode in the boxes below:</p>
    <span class="field">tracking number</span>
    <span class="field">postcode</span>
  </aside>

  <div class="slogan">
    <svg width="846" height="47" viewBox="0 0 846 47" aria-hidden="true">
      <rect width="846" height="47" fill="var(--orange)"/>
      <polygon points="0,0 400,0 430,23.5 400,47 0,47" fill="var(--navy-dark)"/>
    </svg>
    <span class="slogan-name">PARCEL BRISK COURIERS</span>
    <span class="slogan-line">SURE, SAFE &amp; SWIFT</span>
  </div>

  <section class="welcome">
    <h1>Welcome to Parcel Brisk</h1>
    <p>Proin gravida nibh vel velit auctor aliquet. Aenean sollicitudin, lorem quis bibendum auctor, nisi elit consequat ipsum, nec sagittis sem nibh id elit. Duis sed odio sit amet nibh vulputate cursus a sit amet mauris. Morbi accumsan ipsum velit. Nam nec tellus a odio tincidunt auctor a ornare odio. Sed non&nbsp; mauris vitae erat consequat auctor eu in elit. Class aptent taciti sociosqu ad litora torquent per conubia nostra, per inceptos himenaeos. Mauris in erat justo. Nullam ac urna eu felis dapibus condimentum sit amet a augue. Sed non neque elit. Sed ut imperdiet nisi. Proin condimentum fermentum nunc. Etiam pharetra, erat sed fermentum feugiat, velit mauris egestas quam, ut aliquam massa nisl quis neque. Suspendisse in orci enim.</p>
  </section>

  <section class="features">
    <div class="feature" style="left:137px">
      <div class="feature-dot"></div>
      <h3>EZY QUOTE</h3>
      <ul><li>Lorum Ipsum</li><li>Lorum Ipsum</li><li>Lorum Ipsum</li><li>Lorum Ipsum</li></ul>
    </div>
    <div class="feature" style="left:376px">
      <div class="feature-dot"></div>
      <h3>EZY SEND</h3>
      <ul><li>Lorum Ipsum</li><li>Lorum Ipsum</li><li>Lorum Ipsum</li><li>Lorum Ipsum</li></ul>
    </div>
    <div class="feature" style="left:609px">
      <div class="feature-dot"></div>
      <h3>EZY TRACK</h3>
      <ul><li>Lorum Ipsum</li><li>Lorum Ipsum</li><li>Lorum Ipsum</li><li>Lorum Ipsum</li></ul>
    </div>
  </section>

  <div class="newsletter">
    <span class="newsletter-text">Subscribe to our monthly newsletter for latest news updates</span>
    <span class="newsletter-field">email address</span>
    <span class="newsletter-submit">SUBMIT</span>
  </div>

  <footer class="site-footer">
    <ul class="footer-links">
      <li>Terms &amp; Conditions</li><li>Privacy Policy</li><li>FAQs</li><li>Delivery Terms</li><li>Careers</li><li>Contact</li>
    </ul>
    <p class="copyright">© 2013 Parcel Brisk Couriers. All Rights Reserved.</p>
  </footer>
</body>
</html>
```